Professional Services (B-2-B) Business Cards (Front & Back)

Quintarion is a business-to-business professional services company in the legal sector. They typically present to c-suite and executive functions who are looking for providers with expertise, and experience. Our business card should look and feel professional and contemporary, but we are not a startup tech company, so we want the tone to be more mature.

```html
<!DOCTYPE html>
<html lang="en">
<head>
<meta charset="utf-8">
<title>Quintarion Business Cards</title>
<link href="https://fonts.googleapis.com/css2?family=Montserrat:wght@400;500;700&display=swap" rel="stylesheet">
<style>
  :root {
    --backdrop: #2f2f30;
    --navy: #1d2a7a;
    --navy-deep: #17226a;
    --paper: #f6f6f6;
    --ink-grey: #6b6b6b;
    --tab-grey: #9a9a9a;
    --line-navy: #2b3690;
  }
  html, body {
    margin: 0;
    padding: 0;
    width: 1200px;
    height: 900px;
    overflow: hidden;
    background: var(--backdrop);
    font-family: "Montserrat", Arial, sans-serif;
  }
  .canvas {
    position: relative;
    width: 1200px;
    height: 900px;
  }
  .card {
    position: absolute;
    left: 320px;
    width: 560px;
    height: 320px;
    overflow: hidden;
    box-shadow: 0 18px 40px rgba(0,0,0,0.35);
  }
  .card-front { top: 110px; background: var(--paper); }
  .card-back { top: 480px; background: var(--navy); }

  .wordmark {
    position: absolute;
    font-weight: 500;
    letter-spacing: 0.32em;
    text-transform: uppercase;
    display: flex;
    align-items: center;
    gap: 14px;
  }
  .wordmark-mark {
    width: 22px;
    height: 22px;
    display: inline-block;
  }
  .card-front .wordmark {
    top: 44px;
    left: 48px;
    font-size: 20px;
    color: var(--ink-grey);
  }
  .card-front .wordmark-mark { background: var(--navy); }
  .card-back .wordmark {
    top: 138px;
    left: 60px;
    font-size: 24px;
    color: #ffffff;
  }
  .card-back .wordmark-mark { background: #ffffff; }

  .holder {
    position: absolute;
    top: 104px;
    left: 48px;
  }
  .holder-name {
    margin: 0;
    font-size: 17px;
    font-weight: 700;
    color: var(--navy);
  }
  .holder-title {
    margin: 3px 0 0;
    font-size: 11px;
    color: var(--ink-grey);
  }
  .divider-short {
    position: absolute;
    top: 150px;
    left: 48px;
    width: 112px;
    height: 1px;
    background: var(--ink-grey);
    opacity: 0.6;
  }
  .contact {
    position: absolute;
    top: 162px;
    left: 48px;
    margin: 0;
    padding: 0;
    list-style: none;
    font-size: 11px;
    color: var(--ink-grey);
    line-height: 19px;
  }
  .contact li { display: flex; align-items: center; gap: 8px; }
  .contact svg { width: 11px; height: 11px; fill: var(--navy); }

  .divider-long {
    position: absolute;
    top: 232px;
    left: 48px;
    right: 0;
    height: 1px;
    background: var(--line-navy);
  }
  .front-band {
    position: absolute;
    left: 0;
    right: 0;
    bottom: 0;
    height: 24px;
    background: var(--navy);
  }
  .front-tab {
    position: absolute;
    right: 0;
    bottom: 24px;
    width: 0;
    height: 0;
    border-bottom: 10px solid var(--tab-grey);
    border-left: 10px solid transparent;
    border-right: 0;
  }
  .front-tab-fill {
    position: absolute;
    right: 0;
    bottom: 24px;
    width: 96px;
    height: 10px;
    background: var(--tab-grey);
    clip-path: polygon(10px 0, 100% 0, 100% 100%, 0 100%);
  }
  .back-shade {
    position: absolute;
    right: 0;
    top: 0;
    width: 260px;
    height: 100%;
    background: var(--navy-deep);
    opacity: 0.55;
  }
</style>
</head>
<body>
<main class="canvas">
  <section class="card card-front" aria-label="Business card front">
    <div class="wordmark"><span class="wordmark-mark"></span>Quintarion</div>
    <div class="holder">
      <p class="holder-name">Mark Ellison</p>
      <p class="holder-title">President &amp; CEO</p>
    </div>
    <div class="divider-short"></div>
    <ul class="contact">
      <li>
        <svg viewBox="0 0 24 24" aria-hidden="true"><path d="M6.6 10.8a15.1 15.1 0 0 0 6.6 6.6l2.2-2.2a1 1 0 0 1 1-.25 11.4 11.4 0 0 0 3.6.57 1 1 0 0 1 1 1V20a1 1 0 0 1-1 1A17 17 0 0 1 3 4a1 1 0 0 1 1-1h3.5a1 1 0 0 1 1 1c0 1.25.2 2.45.57 3.6a1 1 0 0 1-.25 1z"/></svg>
        (415) 555 - 0182
      </li>
      <li>
        <svg viewBox="0 0 24 24" aria-hidden="true"><path d="M7 1h10a2 2 0 0 1 2 2v18a2 2 0 0 1-2 2H7a2 2 0 0 1-2-2V3a2 2 0 0 1 2-2zm0 3v14h10V4zm5 15.5a1 1 0 1 0 0 2 1 1 0 0 0 0-2z"/></svg>
        (203) 555 - 0147
      </li>
      <li>
        <svg viewBox="0 0 24 24" aria-hidden="true"><path d="M2 5h20v14H2zm2 2v.5l8 5 8-5V7zm0 2.8V17h16V9.8l-8 5z"/></svg>
        mellison@quintarion.tech
      </li>
    </ul>
    <div class="divider-long"></div>
    <div class="front-tab-fill"></div>
    <div class="front-band"></div>
  </section>

  <section class="card card-back" aria-label="Business card back">
    <div class="back-shade"></div>
    <div class="wordmark"><span class="wordmark-mark"></span>Quintarion</div>
  </section>
</main>
</body>
</html>
```